Pixelmora Ads for Leading Telemedicine Provider

Need a variation of this advertisement.

Would like to leave everything the same with white as the dominant color but test the pink circle with a different design style

Target Market(s)

Male / Female from 18-65

Industry/Entity Type

Health

Requirements
Must have
• Use the image attached and test a different background

```html
<!DOCTYPE html>
<html lang="en">
<head>
<meta charset="utf-8">
<title>Ailwell – Free Covid Testing at Home</title>
<link href="https://fonts.googleapis.com/css2?family=Lato:wght@400;700;900&display=swap" rel="stylesheet">
<style>
  :root {
    --white: #ffffff;
    --navy: #0b1960;
    --cyan: #22dcfc;
    --sky: #7fb8f5;
    --violet: #d78ff0;
    --button: #d895ef;
    --scene-light: #f6f1e2;
    --scene-warm: #eadcb4;
    --icon-tone: #e3e8f0;
  }
  * { margin: 0; padding: 0; box-sizing: border-box; }
  html, body { width: 1200px; height: 1200px; overflow: hidden; background: var(--white); }
  .ad {
    position: relative;
    width: 1200px;
    height: 1200px;
    background: var(--white);
    font-family: "Lato", sans-serif;
    overflow: hidden;
  }
  .ad__blobs { position: absolute; inset: 0; }
  .brand {
    position: absolute;
    left: 84px;
    top: 62px;
    font-size: 112px;
    font-weight: 900;
    color: var(--navy);
    letter-spacing: -2px;
    line-height: 1;
  }
  .headline {
    position: absolute;
    left: 88px;
    top: 232px;
    font-size: 148px;
    font-weight: 900;
    line-height: 173px;
    letter-spacing: -2px;
  }
  .headline__line {
    display: block;
    width: fit-content;
    background: linear-gradient(90deg, var(--cyan) 0%, var(--sky) 50%, var(--violet) 100%);
    -webkit-background-clip: text;
    background-clip: text;
    color: transparent;
  }
  .cta {
    position: absolute;
    left: 234px;
    top: 911px;
    width: 292px;
    height: 69px;
    border-radius: 6px;
    background: var(--button);
    color: var(--white);
    font-size: 30px;
    font-weight: 400;
    letter-spacing: -0.5px;
    display: flex;
    align-items: center;
    justify-content: center;
  }
  .url {
    position: absolute;
    left: 81px;
    top: 1106px;
    font-size: 35px;
    font-weight: 700;
    color: var(--white);
    letter-spacing: -0.3px;
  }
  .virus-badge {
    position: absolute;
    left: 944px;
    top: 440px;
    width: 120px;
    height: 120px;
    border-radius: 50%;
    background: var(--icon-tone);
  }
  .scene {
    position: absolute;
    left: 591px;
    top: 580px;
    width: 556px;
    height: 550px;
    border-radius: 24px;
    background: linear-gradient(160deg, var(--scene-light) 0%, var(--scene-warm) 100%);
  }
</style>
</head>
<body>
  <main class="ad">
    <svg class="ad__blobs" width="1200" height="1200" viewBox="0 0 1200 1200" aria-hidden="true">
      <defs>
        <linearGradient id="blobTop" x1="0" y1="0" x2="1" y2="1">
          <stop offset="0" stop-color="#22dcfc"/>
          <stop offset="0.55" stop-color="#9fb0f2"/>
          <stop offset="1" stop-color="#d393ef"/>
        </linearGradient>
        <linearGradient id="blobBottom" x1="0" y1="0" x2="1" y2="1">
          <stop offset="0.2" stop-color="#22dcfc"/>
          <stop offset="0.6" stop-color="#9aaff2"/>
          <stop offset="1" stop-color="#d98ff0"/>
        </linearGradient>
      </defs>
      <!-- soft outer wave layers -->
      <path class="wave wave--top" fill="url(#blobTop)" opacity="0.18"
        d="M650,0 C640,140 730,240 870,236 C990,232 1045,300 1065,400 C1085,490 1130,530 1200,530 V0 Z"/>
      <path class="wave wave--bottom" fill="url(#blobBottom)" opacity="0.18"
        d="M0,660 C110,676 170,750 195,880 C220,1000 270,1035 420,1038 C590,1041 670,1090 695,1200 H0 Z"/>
      <!-- main blobs -->
      <path class="blob blob--top" fill="url(#blobTop)"
        d="M689,0 C680,120 760,205 880,202 C1000,199 1070,260 1090,360 C1110,450 1140,490 1200,490 V0 Z"/>
      <path class="blob blob--bottom" fill="url(#blobBottom)"
        d="M0,706 C90,720 140,780 165,900 C190,1020 230,1070 400,1072 C560,1074 630,1110 652,1200 H0 Z"/>
      <!-- thin outline accents -->
      <path class="contour contour--top" fill="none" stroke="#b7a6f2" stroke-width="3" stroke-dasharray="2 12" stroke-linecap="round"
        d="M620,0 C610,160 710,270 860,268 C975,266 1025,330 1043,430 C1060,520 1120,570 1200,572"/>
      <path class="contour contour--bottom" fill="none" stroke="#9ec3f6" stroke-width="3" stroke-dasharray="2 12" stroke-linecap="round"
        d="M0,615 C130,632 195,715 222,860 C248,985 305,1004 440,1006 C620,1008 710,1070 740,1200"/>
    </svg>

    <div class="brand">Ailwell</div>

    <h1 class="headline">
      <span class="headline__line">Free Covid</span>
      <span class="headline__line">Testing at</span>
      <span class="headline__line">Home</span>
    </h1>

    <div class="cta">BOOK NOW</div>

    <div class="url">https://ailwell.org/covid-testing</div>

    <div class="virus-badge" role="img" aria-label="Icon of a green virus crossed out inside a grey circle"></div>

    <div class="scene" role="img" aria-label="Illustration of a woman at her front door greeting a masked courier holding a clipboard, with a potted plant, welcome mat and a yellow tick badge"></div>
  </main>
</body>
</html>
```